Naturopath needs product label for new essence range

I need a label design for a new range of Essences. The essences resonate with the energetic chakra centres of the body to shift blockages, balance them and lead to transformation and spiritual growth. I have a logo to be used. The name of the essence range is Corvanthe which means "to reveal truth or True Nature". The first essence resonates with the Base Chakra and is called "Base" I would like a strong bold red colour to feature in the design. The label size would be about 76mm x 27mm. See below for the required information to be on the label.
Updates

Hi everyone, I'm not sure if it's important to help with the design, but I've just uploaded the logo in several different formats. Thanks for all your submissions. Also please use a deep red colour, the example from the colour wheel is too light. Kind regards, Dorian

Target Market(s)

Adults open to alternative therapies and spiritual development

Industry/Entity Type

Product

Colors
eb1f27

Requirements
Must have
• The logo. A deep red colour as the background or part of the background
"Base"
corvantheessences.example.au
Batch
Expiry
Ingredients: vibrational essence of herbs, flowers and crystals, purified water, brandy (approx 12.5% alcohol)
20ml
Dosage: 7 drops once a day

```html
<!DOCTYPE html>
<html lang="en">
<head>
<meta charset="utf-8">
<title>Corvanthe Essences – Base label</title>
<link rel="stylesheet" href="https://fonts.googleapis.com/css2?family=Cinzel:wght@500&family=Tinos:wght@400;700&display=swap">
<style>
  :root {
    --label-red: #eb1f27;
    --brand-gold: #d6a62c;
    --text-white: #ffffff;
    --text-dark: #1a0a0a;
  }
  html, body {
    margin: 0;
    padding: 0;
    overflow: hidden;
    background: var(--label-red);
  }
  .label {
    position: relative;
    width: 1200px;
    height: 430px;
    background: var(--label-red);
    overflow: hidden;
  }
  .brand-mark {
    position: absolute;
    left: 678px;
    top: 78px;
    width: 110px;
    height: 110px;
    transform: translateX(-50%);
  }
  .brand-name {
    position: absolute;
    left: 0;
    width: 1356px;
    top: 238px;
    margin: 0;
    text-align: center;
    font-family: "Cinzel", "Times New Roman", serif;
    font-weight: 500;
    font-size: 44px;
    letter-spacing: 6px;
    line-height: 1;
    color: var(--brand-gold);
  }
  .brand-name .brand-sub {
    display: block;
    margin-top: 14px;
    font-size: 28px;
    letter-spacing: 5px;
  }
  .website {
    position: absolute;
    left: 0;
    width: 1356px;
    top: 318px;
    margin: 0;
    text-align: center;
    font-family: "Tinos", "Times New Roman", serif;
    font-weight: 700;
    font-size: 20px;
    color: var(--text-white);
  }
  .product-name {
    position: absolute;
    left: 0;
    width: 1356px;
    top: 350px;
    margin: 0;
    text-align: center;
    font-family: "Tinos", "Times New Roman", serif;
    font-weight: 400;
    font-size: 46px;
    line-height: 1;
    transform: scaleX(0.88);
    color: var(--text-dark);
  }
  .product-info {
    position: absolute;
    left: 943px;
    top: 170px;
    width: 430px;
    height: 90px;
    transform: rotate(-90deg);
    transform-origin: 215px 45px;
    text-align: center;
    font-family: "Tinos", "Times New Roman", serif;
    font-size: 14.4px;
    line-height: 17px;
    color: var(--text-white);
  }
  .product-info p { margin: 0; white-space: nowrap; }
</style>
</head>
<body>
  <main class="label">
    <svg class="brand-mark" viewBox="0 0 110 110" aria-hidden="true">
      <circle cx="55" cy="55" r="50" fill="var(--brand-gold)"/>
    </svg>
    <h1 class="brand-name">Corvanthe<span class="brand-sub">Essences</span></h1>
    <p class="website">corvantheessences.example.au</p>
    <h2 class="product-name">BASE</h2>
    <section class="product-info">
      <p>Ingredients: vibrational essence of herbs, flowers and crystals,</p>
      <p>purified water, brandy (approx 12.5% alcohol)</p>
      <p>(batch #0012030&nbsp; expires: 01/12/2015</p>
      <p>Dosage: 7 drops once a day</p>
      <p>20ml</p>
    </section>
  </main>
</body>
</html>
```